Modern Medical Optometry Website

We need mordern, Patient friendly website. Easy to navigate and enhance our advance medical technology and excellent patient care.
1. HOME PAGE
2. OUR TEAM PAGE
3. EYECARE PAGE - VISION SERVICES, EYE EXAMS, KERATOCONUS CENTER, GLAUCOMA , DIABITES, VELMORIN EXAM, DIGITAL RETINAL, OCT.
4. MYOPIA CONTROL CLINIC
5. DRY EYE CLINIC
6. EYEWEAR
7. PATIENT CENTER - BLOG
7. CONTACT US
This is our current website www.lumvarta.com
and We want to add more content and a cleaner design like these website
http://norvellbrookclinic.com/
https://www.tqvamori.com/

```html
<!DOCTYPE html>
<html lang="en">
<head>
<meta charset="utf-8">
<title>Lumvarta Optometry – Testimonials</title>
<link href="https://fonts.googleapis.com/css2?family=Montserrat:wght@700;800&family=Raleway:wght@400;500;600;700&display=swap" rel="stylesheet">
<style>
:root{
  --teal:#0b8fb3;
  --teal-dark:#0a7f9f;
  --yellow:#fbdf2c;
  --footer:#f8e35a;
  --ink:#2b2b2b;
  --muted:#8a8a8a;
  --white:#ffffff;
  --pill:#2f2f2f;
  --play:#e0262a;
}
*{box-sizing:border-box;margin:0;padding:0}
html,body{width:1200px;height:3458px;overflow:hidden}
body{font-family:"Raleway",sans-serif;color:var(--ink);background:var(--white);position:relative}
.topbar{height:52px;background:var(--teal)}
.site-header{height:136px;background:var(--white);position:relative}
.brand{position:absolute;left:77px;top:-31px;width:110px;height:143px;background:var(--white);display:flex;flex-direction:column;align-items:center;justify-content:center;gap:10px}
.brand-mark{width:58px;height:58px;background:var(--yellow)}
.brand-name{font-size:15px;font-weight:500;color:#7a7a7a;text-align:center;line-height:1.05;letter-spacing:.5px}
.main-nav a{position:absolute;top:111px;font-size:16px;color:#8f8f8f;text-decoration:none;letter-spacing:.3px;transform:translateY(-52px)}
.main-nav a.active{color:var(--teal);font-weight:600}
.search{position:absolute;left:1102px;top:58px}
.hero{position:relative;height:573px;background:linear-gradient(100deg,#1a93b0 0%,#2aa3bf 55%,#1f97b5 100%);overflow:hidden}
.hero-backdrop{position:absolute;right:0;top:0;width:560px;height:573px;background:linear-gradient(120deg,rgba(40,160,190,0) 0%,rgba(90,190,210,.5) 60%,rgba(30,140,170,.6) 100%)}
.hero-title{position:absolute;left:80px;top:130px;font-family:"Montserrat",sans-serif;font-weight:800;font-size:62px;line-height:66px;color:var(--white);letter-spacing:3px;text-shadow:0 3px 6px rgba(0,0,0,.35)}
.hero-text{position:absolute;left:79px;top:280px;width:460px;font-size:14.5px;line-height:26px;color:var(--white);font-weight:600}
.btn-appt{position:absolute;left:77px;top:385px;width:240px;height:53px;background:var(--yellow);color:var(--ink);font-size:17.5px;display:flex;align-items:center;justify-content:center;letter-spacing:.3px}
.hero-portrait{position:absolute;left:567px;top:35px}
.section-title{position:absolute;top:840px;width:100%;text-align:center;font-family:"Montserrat",sans-serif;font-weight:700;font-size:36px;color:var(--teal);letter-spacing:.5px}
.section-intro{position:absolute;top:898px;left:100px;width:1000px;text-align:center;font-size:14px;line-height:26px;color:var(--muted);letter-spacing:.2px}
.testimonials{position:absolute;top:1010px;left:77px;width:1045px;display:grid;grid-template-columns:repeat(3,323px);column-gap:38px;row-gap:42px}
.card{height:457px;background:var(--teal);color:var(--white);display:flex;flex-direction:column}
.card.highlight{background:var(--yellow);color:var(--ink)}
.card.center{grid-column:2}
.card-media{height:229px;position:relative;display:flex;align-items:center;justify-content:center}
.play{width:52px;height:34px;background:var(--play);border-radius:8px;display:flex;align-items:center;justify-content:center}
.card-quote{padding:16px 18px 0;font-size:14.5px;line-height:26px;letter-spacing:.2px}
.card-name{padding:24px 18px 0;font-size:15px;font-weight:700;letter-spacing:.2px}
.site-footer{position:absolute;top:3061px;left:0;width:1200px;height:397px;background:var(--footer)}
.footer-col{position:absolute;top:40px;width:330px}
.footer-col h3{font-size:21px;font-weight:700;color:var(--teal);margin-bottom:18px}
.contact-line{display:flex;gap:18px;font-size:14.5px;line-height:21px;color:#3a3a3a;margin-bottom:11px}
.contact-line svg{flex:0 0 22px}
.btn-map{position:absolute;top:258px;width:280px;height:41px;border-radius:21px;background:var(--pill);color:var(--white);font-size:15px;display:flex;align-items:center;padding-left:17px;gap:22px}
.hours p{font-size:14.5px;line-height:28px;color:#3a3a3a}
.hours b{font-weight:700;color:#222}
.hours .note{line-height:20px;margin-top:4px}
.social{position:absolute;top:258px;display:flex;gap:12px}
.social span{width:40px;height:40px;border-radius:50%;background:var(--pill)}
.social span:first-child{background:var(--teal)}
.copyright{position:absolute;top:361px;width:100%;text-align:center;font-size:13.5px;color:#6b6b6b}
.copyright b{color:var(--teal)}
</style>
</head>
<body>
<div class="topbar"></div>
<header class="site-header">
  <div class="brand"><span class="brand-mark"></span><span class="brand-name">LUMVARTA<br>OPTOMETRY</span></div>
  <nav class="main-nav">
    <a href="#" class="active" style="left:220px">HOME</a>
    <a href="#" style="left:309px">OUR TEAM</a>
    <a href="#" style="left:537px">MYOPIA CONTROL CLINIC</a>
    <a href="#" style="left:779px">EYEWEAR</a>
    <a href="#" style="left:888px">BLOG</a>
    <a href="#" style="left:970px">CONTACT US</a>
  </nav>
  <svg class="search" width="22" height="22" viewBox="0 0 22 22" fill="none" stroke="#0b8fb3" stroke-width="1.8"><circle cx="9" cy="9" r="7"/><path d="M14 14l6 6"/></svg>
</header>

<section class="hero">
  <div class="hero-backdrop"></div>
  <svg class="hero-portrait" width="500" height="500" viewBox="0 0 500 500" role="img" aria-label="Portrait of a smiling woman wearing glasses">
    <defs><radialGradient id="face" cx="55%" cy="50%" r="55%"><stop offset="0" stop-color="#f2c7a8"/><stop offset=".6" stop-color="#d9a07e"/><stop offset="1" stop-color="#8f6a55"/></radialGradient></defs>
    <circle cx="249" cy="248" r="248" fill="#9fa8ad" opacity=".85"/>
    <circle cx="249" cy="248" r="208" fill="url(#face)"/>
    <circle cx="249" cy="248" r="208" fill="none" stroke="#fbdf2c" stroke-width="20"/>
  </svg>
  <h1 class="hero-title">WHAT OUR<br>CLIENTS SAY</h1>
  <p class="hero-text">Lorem ipsum dolor sit amet, consectetur adipiscing elit, sed aliqua. Ut enim ad minim veniam, quis nostrud exercitation ullamco laboris nisi ut aliquip ex ea commodo consequat.</p>
  <a class="btn-appt">MAKE AN APPOINTMENT</a>
</section>

<h2 class="section-title">TESTIMONIALS</h2>
<p class="section-intro">Lorem Ipsum is simply dummy text of the printing and typesetting industry. Lorem Ipsum has been the industry's standard dummy text ever since the 1500s, when an unknown printer took a galley of type and scrambled it to make a type specimen book.</p>

<main class="testimonials">
  <article class="card"><div class="card-media" role="img" aria-label="Video still of a woman in dark glasses" style="background:linear-gradient(135deg,#5a4a42,#2e2623)"><span class="play"><svg width="14" height="16"><path d="M2 1l11 7-11 7z" fill="#fff"/></svg></span></div><p class="card-quote">Lorem Ipsum is simply dummy text of the printing and typesetting industry. Lorem Ipsum has been the industry's standard dummy text ever since the 1500s, when an unknown printer took a galley .</p><p class="card-name">_ CLIENT NAME</p></article>
  <article class="card highlight"><div class="card-media" role="img" aria-label="Black and white video still of a woman in glasses" style="background:linear-gradient(135deg,#4a4a4a,#141414)"><span class="play"><svg width="14" height="16"><path d="M2 1l11 7-11 7z" fill="#fff"/></svg></span></div><p class="card-quote">Lorem Ipsum is simply dummy text of the printing and typesetting industry. Lorem Ipsum has been the industry's standard dummy text ever since the 1500s, when an unknown printer took a galley .</p><p class="card-name">_ CLIENT NAME</p></article>
  <article class="card"><div class="card-media" role="img" aria-label="Video still of a woman against a grey wall" style="background:linear-gradient(135deg,#8c8c88,#55524f)"><span class="play"><svg width="14" height="16"><path d="M2 1l11 7-11 7z" fill="#fff"/></svg></span></div><p class="card-quote">Lorem Ipsum is simply dummy text of the printing and typesetting industry. Lorem Ipsum has been the industry's standard dummy text ever since the 1500s, when an unknown printer took a galley .</p><p class="card-name">_ CLIENT NAME</p></article>
  <article class="card"><div class="card-media" role="img" aria-label="Video still of a young girl in glasses in a library" style="background:linear-gradient(135deg,#6b4a2e,#3a2a1e)"><span class="play"><svg width="14" height="16"><path d="M2 1l11 7-11 7z" fill="#fff"/></svg></span></div><p class="card-quote">Lorem Ipsum is simply dummy text of the printing and typesetting industry. Lorem Ipsum has been the industry's standard dummy text ever since the 1500s, when an unknown printer took a galley .</p><p class="card-name">_ CLIENT NAME</p></article>
  <article class="card"><div class="card-media" role="img" aria-label="Video still of a young man in glasses" style="background:linear-gradient(135deg,#4a4644,#1e1c1b)"><span class="play"><svg width="14" height="16"><path d="M2 1l11 7-11 7z" fill="#fff"/></svg></span></div><p class="card-quote">Lorem Ipsum is simply dummy text of the printing and typesetting industry. Lorem Ipsum has been the industry's standard dummy text ever since the 1500s, when an unknown printer took a galley .</p><p class="card-name">_ CLIENT NAME</p></article>
  <article class="card"><div class="card-media" role="img" aria-label="Video still of a young man in glasses and a checked shirt" style="background:linear-gradient(135deg,#5a5350,#28231f)"><span class="play"><svg width="14" height="16"><path d="M2 1l11 7-11 7z" fill="#fff"/></svg></span></div><p class="card-quote">Lorem Ipsum is simply dummy text of the printing and typesetting industry. Lorem Ipsum has been the industry's standard dummy text ever since the 1500s, when an unknown printer took a galley .</p><p class="card-name">_ CLIENT NAME</p></article>
  <article class="card"><div class="card-media" role="img" aria-label="Video still of a woman adjusting her glasses" style="background:linear-gradient(135deg,#3f5a66,#2a2422)"><span class="play"><svg width="14" height="16"><path d="M2 1l11 7-11 7z" fill="#fff"/></svg></span></div><p class="card-quote">Lorem Ipsum is simply dummy text of the printing and typesetting industry. Lorem Ipsum has been the industry's standard dummy text ever since the 1500s, when an unknown printer took a galley .</p><p class="card-name">_ CLIENT NAME</p></article>
  <article class="card"><div class="card-media" role="img" aria-label="Video still of a red-haired woman in glasses" style="background:linear-gradient(135deg,#6a4a38,#2c2522)"><span class="play"><svg width="14" height="16"><path d="M2 1l11 7-11 7z" fill="#fff"/></svg></span></div><p class="card-quote">Lorem Ipsum is simply dummy text of the printing and typesetting industry. Lorem Ipsum has been the industry's standard dummy text ever since the 1500s, when an unknown printer took a galley .</p><p class="card-name">_ CLIENT NAME</p></article>
  <article class="card"><div class="card-media" role="img" aria-label="Video still of a woman in round glasses and earrings" style="background:linear-gradient(135deg,#5c4d44,#2a2320)"><span class="play"><svg width="14" height="16"><path d="M2 1l11 7-11 7z" fill="#fff"/></svg></span></div><p class="card-quote">Lorem Ipsum is simply dummy text of the printing and typesetting industry. Lorem Ipsum has been the industry's standard dummy text ever since the 1500s, when an unknown printer took a galley .</p><p class="card-name">_ CLIENT NAME</p></article>
  <article class="card center"><div class="card-media" role="img" aria-label="Video still of a curly-haired woman in glasses" style="background:linear-gradient(135deg,#4f3a33,#1f1816)"><span class="play"><svg width="14" height="16"><path d="M2 1l11 7-11 7z" fill="#fff"/></svg></span></div><p class="card-quote">Lorem Ipsum is simply dummy text of the printing and typesetting industry. Lorem Ipsum has been the industry's standard dummy text ever since the 1500s, when an unknown printer took a galley .</p><p class="card-name">_ CLIENT NAME</p></article>
</main>

<footer class="site-footer">
  <div class="footer-col" style="left:80px">
    <h3>Lumvarta Optometry</h3>
    <div class="contact-line"><svg width="22" height="20" viewBox="0 0 24 24" fill="#0b8fb3"><path d="M6.6 10.8a15 15 0 006.6 6.6l2.2-2.2c.3-.3.7-.4 1-.2 1.1.4 2.3.6 3.6.6.6 0 1 .4 1 1V20c0 .6-.4 1-1 1A17 17 0 013 4c0-.6.4-1 1-1h3.5c.6 0 1 .4 1 1 0 1.3.2 2.5.6 3.6.1.3 0 .7-.2 1z"/></svg><span>555-201-4410</span></div>
    <div class="contact-line"><svg width="22" height="20" viewBox="0 0 24 24" fill="#0b8fb3"><rect x="6" y="2" width="12" height="6"/><rect x="2" y="9" width="20" height="9" rx="2"/><rect x="6" y="15" width="12" height="7"/></svg><span>555-201-4470</span></div>
    <div class="contact-line"><svg width="22" height="20" viewBox="0 0 24 24" fill="#0b8fb3"><rect x="2" y="5" width="20" height="14" rx="1"/><path d="M2 6l10 7 10-7" stroke="#f8e35a" stroke-width="1.6" fill="none"/></svg><span>info@lumvarta.com</span></div>
    <div class="contact-line"><svg width="22" height="20" viewBox="0 0 24 24" fill="#0b8fb3"><path d="M12 2a7 7 0 00-7 7c0 5 7 13 7 13s7-8 7-13a7 7 0 00-7-7zm0 9.5A2.5 2.5 0 1112 6a2.5 2.5 0 010 5.5z"/></svg><span>4820 Harlow Ave., Brenwick,<br>CA 90512</span></div>
  </div>
  <a class="btn-map" style="left:78px">Get directions on the map <svg width="32" height="10"><path d="M0 5h28M23 1l5 4-5 4" stroke="#1aa6cf" stroke-width="1.6" fill="none"/></svg></a>

  <div class="footer-col" style="left:436px">
    <h3>Corliss Grove</h3>
    <div class="contact-line"><svg width="22" height="20" viewBox="0 0 24 24" fill="#0b8fb3"><path d="M6.6 10.8a15 15 0 006.6 6.6l2.2-2.2c.3-.3.7-.4 1-.2 1.1.4 2.3.6 3.6.6.6 0 1 .4 1 1V20c0 .6-.4 1-1 1A17 17 0 013 4c0-.6.4-1 1-1h3.5c.6 0 1 .4 1 1 0 1.3.2 2.5.6 3.6.1.3 0 .7-.2 1z"/></svg><span>555-318-2260</span></div>
    <div class="contact-line"><svg width="22" height="20" viewBox="0 0 24 24" fill="#0b8fb3"><rect x="2" y="5" width="20" height="14" rx="1"/><path d="M2 6l10 7 10-7" stroke="#f8e35a" stroke-width="1.6" fill="none"/></svg><span>corlissgrove@lumvarta.com</span></div>
    <div class="contact-line"><svg width="22" height="20" viewBox="0 0 24 24" fill="#0b8fb3"><path d="M12 2a7 7 0 00-7 7c0 5 7 13 7 13s7-8 7-13a7 7 0 00-7-7zm0 9.5A2.5 2.5 0 1112 6a2.5 2.5 0 010 5.5z"/></svg><span>1190 Tamsen St.,Suite 4,<br>Corliss Grove, CA 90527</span></div>
  </div>
  <a class="btn-map" style="left:435px">Get directions on the map <svg width="32" height="10"><path d="M0 5h28M23 1l5 4-5 4" stroke="#1aa6cf" stroke-width="1.6" fill="none"/></svg></a>

  <div class="footer-col hours" style="left:792px">
    <h3>Opening Hours</h3>
    <p>Monday - Thursday : <b>9 am - 6 pm</b></p>
    <p>Friday : <b>8.30 am - 5 pm</b></p>
    <p>Saturday &nbsp;: <b>8.30 am- 5 pm</b></p>
    <p>Closed on <b>Sundays</b></p>
    <p class="note">Please keep in mind we are closed<br>for <b>lunch 1-2 pm</b></p>
  </div>
  <div class="social" style="left:792px"><span></span><span></span><span></span><span></span></div>

  <p class="copyright">Copyright © <b>LUMVARTA OPTOMETRY</b> - 2019 . All right Resereved</p>
</footer>
</body>
</html>
```